Solar Advertising Flier to generate Biz

I need a advertisement that generates business to be used in a mailer for marketing purposes.

Im attaching a file that is a an idea of advertisement.
I do not want the "ZVN" specific information on it.
I want the background solar panels.
Same information as the ad.
And I've attached my Logo - I want the color scheme to match this.

Thank you

Target Market(s)

Middle to Upper Class Home Owners

Industry/Entity Type

Solar Energy

Requirements
Must have
• A call to action
• A professional look
Nice to have
• A family
• Great looking solar panels
Should not have
• Cartoons

```html
<!DOCTYPE html>
<html lang="en">
<head>
<meta charset="utf-8">
<title>Bright Haven Energy – Go Solar Flyer</title>
<link rel="stylesheet" href="https://fonts.googleapis.com/css2?family=Lato:wght@400;700;900&family=Oswald:wght@500;600&display=swap">
<style>
  :root{
    --blue:#1a8fd0;
    --blue-deep:#0a86c8;
    --green:#8cc63f;
    --green-light:#a9d346;
    --ink:#1d1d1b;
    --white:#ffffff;
    --page:#e9e9e9;
  }
  *{margin:0;padding:0;box-sizing:border-box}
  html,body{width:1200px;height:1200px;overflow:hidden;background:var(--page)}
  .flyer{
    position:absolute;left:190px;top:20px;width:893px;height:1265px;
    transform:scale(0.917);transform-origin:0 0;
    background:var(--white);overflow:hidden;
    font-family:"Lato",Arial,sans-serif;color:var(--ink);
  }
  .flyer-art{position:absolute;inset:0}
  .brand{position:absolute;left:50px;top:70px;width:320px;text-align:center}
  .brand-dot{width:120px;height:120px;border-radius:50%;background:var(--green);margin:0 auto 22px}
  .brand-name{font-weight:700;color:var(--blue);font-size:34px;line-height:1.1}
  .ribbon{position:absolute;left:138px;top:378px;width:322px;height:44px;background:var(--blue);
    color:var(--white);font-weight:900;font-size:28px;line-height:44px;text-align:center;
    clip-path:polygon(4% 0,100% 0,100% 100%,0 100%)}
  .benefits{position:absolute;left:55px;top:450px;width:370px;list-style:none}
  .benefits li{position:relative;padding-left:30px;font-size:23px;line-height:31px;margin-bottom:20px}
  .benefits li::before{content:"";position:absolute;left:2px;top:9px;width:14px;height:14px;border:1.5px solid var(--ink);border-radius:50%}
  .benefits b{font-weight:900}
  .headline{position:absolute;left:484px;top:690px;font-weight:900;font-size:64px;color:var(--blue);letter-spacing:1px}
  .how-title{position:absolute;left:44px;top:812px;font-weight:900;font-size:29px;color:var(--blue)}
  .how-text{position:absolute;left:45px;top:855px;width:795px;font-size:23px;line-height:36px;text-align:justify}
  .how-text b{font-weight:900}
  .rebate{position:absolute;left:20px;top:1075px;width:200px;text-align:center;font-weight:900;line-height:1}
  .rebate-lead{color:var(--blue);font-size:29px}
  .rebate-sub{font-size:25px;margin-top:2px}
  .rebate-amount{color:var(--green);font-size:58px;margin:6px 0 2px}
  .rebate-tail{font-size:27px}
  .contact{position:absolute;right:36px;top:1120px;text-align:right;color:var(--white)}
  .contact-lead{font-family:"Oswald",Arial,sans-serif;font-weight:500;font-size:27px}
  .contact-phone{font-family:"Oswald",Arial,sans-serif;font-weight:600;font-size:46px;line-height:1.15;letter-spacing:1px}
  .contact-web{font-size:27px}
</style>
</head>
<body>
<main class="flyer">
  <svg class="flyer-art" width="893" height="1265" viewBox="0 0 893 1265">
    <defs>
      <linearGradient id="houseFade" x1="0" y1="0" x2="0" y2="1">
        <stop offset="0" stop-color="#eef0f2"/><stop offset="1" stop-color="#f7f7f7"/>
      </linearGradient>
      <linearGradient id="familyTone" x1="0" y1="0" x2="1" y2="1">
        <stop offset="0" stop-color="#d9744a"/><stop offset=".45" stop-color="#8fb2d4"/><stop offset="1" stop-color="#c9a184"/>
      </linearGradient>
      <linearGradient id="workerTone" x1="0" y1="0" x2="1" y2="1">
        <stop offset="0" stop-color="#e9ddc9"/><stop offset=".5" stop-color="#8aa7d6"/><stop offset="1" stop-color="#2f4f9e"/>
      </linearGradient>
    </defs>
    <rect x="0" y="380" width="893" height="720" fill="url(#houseFade)" role="img" aria-label="Faint photo of a house with solar panels on its roof"/>
    <path d="M430 0H893V380C800 410 690 415 560 395C470 370 405 280 400 180C397 110 410 45 430 0Z" fill="url(#familyTone)" role="img" aria-label="Photo of a smiling family in front of a house with a solar panel roof"/>
    <path d="M455 0C415 50 397 110 399 165" fill="none" stroke="var(--blue)" stroke-width="12"/>
    <path d="M401 230C415 310 470 370 560 400C690 420 800 415 893 390" fill="none" stroke="var(--green)" stroke-width="10"/>
    <path d="M0 380C120 320 300 300 440 332" fill="none" stroke="var(--blue)" stroke-width="6"/>
    <path d="M0 410C120 345 300 322 430 340" fill="none" stroke="var(--green)" stroke-width="14"/>
    <path d="M43 385C150 345 300 330 428 343V750Q428 770 408 770H63Q43 770 43 750Z" fill="var(--green-light)"/>
    <path d="M428 422H460L428 452Z" fill="var(--blue-deep)"/>
    <circle cx="668" cy="500" r="160" fill="url(#workerTone)" stroke="var(--green)" stroke-width="8" role="img" aria-label="Photo of a smiling solar installer in a hard hat working on roof panels"/>
    <path d="M250 1120C450 1050 700 1020 893 1060V1265H250Z" fill="var(--blue-deep)"/>
    <path d="M250 1108C450 1038 700 1008 893 1048" fill="none" stroke="var(--green)" stroke-width="10"/>
    <circle cx="115" cy="1185" r="158" fill="var(--white)" stroke="var(--green)" stroke-width="7"/>
    <path d="M5 1080C30 1055 60 1035 95 1028" fill="none" stroke="var(--blue)" stroke-width="8"/>
  </svg>

  <div class="brand">
    <div class="brand-dot"></div>
    <div class="brand-name">Bright Haven Energy</div>
  </div>

  <div class="ribbon">WE MAKE IT EASY</div>
  <ul class="benefits">
    <li><b>$0 Down</b>, no upfront cost.</li>
    <li><b>Save 95%</b> off your utility bill.</li>
    <li>Protect yourself from rising energy costs.</li>
    <li>Provide clean, reliable energy for your family <b>powered by the sun</b>.</li>
  </ul>

  <h1 class="headline">GO SOLAR</h1>

  <h2 class="how-title">HOW IT WORKS...</h2>
  <p class="how-text">Your solar system allows you to <b>generate your own clean power</b> and COSTS LESS than your current utility company. Simply pay by the month, like you do now...but at a LOWER rate and <b>START SAVING IMMEDIATELY.</b></p>

  <div class="rebate">
    <div class="rebate-lead">CALL TODAY</div>
    <div class="rebate-sub">AND RECEIVE</div>
    <div class="rebate-amount">$ 500</div>
    <div class="rebate-tail">CASH REBATE</div>
  </div>

  <div class="contact">
    <div class="contact-lead">Call Today For A No Obligation Consulting</div>
    <div class="contact-phone">555-014-2368</div>
    <div class="contact-web">www.brighthavenenergy.com</div>
  </div>
</main>
</body>
</html>
```